GraniteLoop. Customer needs to know about us, what services we provide & contact us

We are a waste tire recycling company. Our primary focus is on providing a sustainable and cost effective service focusing on: Waste Tire Management, Hassle Free Scheduling for Tire Collection, Mobile Shredding & Special site cleanup services. GraniteLoop will be producing TDF, Clean Tire Wire & further materials.
Please look at https://quorvalwheel.example
Please look at https://bandimacorp.example

This is the look and feel of what we want

I have attached a word document with our website info.

Target Market(s)

Tire Install Companies. Such as paltonhaul.example. TDF Purchasers such as kevrofuel.example.

Industry/Entity Type

Waste Tire Recycling

Coding

Coded - Design and coding required

Number of Pages Required

3 page

Font styles to use
Other font styles liked:
• Look at our logo

Requirements
Must have
• We need a 3 page setup for About Us, Services & Contact Us. Contact us should be a form them can fill out and submit to us Images that are related to waste tire recycling. Clean, modern, innovative.
Nice to have
• The color and feel of the website should work with our logo that we did with artmarketly
Should not have
• Anything progressive, political or "woke"

```html
<!DOCTYPE html>
<html lang="en">
<head>
<meta charset="utf-8">
<title>GraniteLoop – Waste Tire Recycling</title>
<link href="https://fonts.googleapis.com/css2?family=Oswald:wght@400;500;700&family=Open+Sans:wght@400;600;700&display=swap" rel="stylesheet">
<style>
:root{
  --green:#1c9b43;
  --green-dark:#137a33;
  --ink:#1b1d1e;
  --char:#2a2c2d;
  --mist:#e4edf1;
  --paper:#ffffff;
  --grey:#f0f2f3;
  --muted:#6a7074;
}
*{box-sizing:border-box;margin:0;padding:0}
html,body{width:1200px;height:2744px;overflow:hidden}
body{font-family:"Open Sans",Arial,sans-serif;color:var(--ink);background:var(--paper)}
.page{width:1200px;height:2744px;display:flex;flex-direction:column}
h1,h2,h3,.display{font-family:"Oswald",Arial Narrow,sans-serif;text-transform:uppercase}
.btn{display:inline-block;background:var(--green);color:#fff;font:600 13px "Open Sans",sans-serif;text-transform:uppercase;padding:11px 26px;letter-spacing:.5px}
.brand{display:flex;align-items:center;gap:10px;font:700 30px "Oswald",sans-serif;color:var(--green)}
.brand .dot{width:26px;height:26px;border-radius:50%;background:var(--green)}
.eyebrow{font:600 12px "Open Sans",sans-serif;color:var(--green);letter-spacing:1px;text-transform:uppercase}

/* header */
.site-header{height:80px;display:flex;align-items:center;justify-content:space-between;padding:0 120px}
.nav{display:flex;gap:34px;font:600 12px "Open Sans",sans-serif;text-transform:uppercase}
.header-contact{display:flex;align-items:center;gap:18px;font-size:12px}
.header-contact strong{display:block;font-size:15px}
.social{display:flex;gap:8px}
.social span{width:26px;height:26px;border-radius:50%;background:var(--ink)}

/* hero */
.hero{height:400px;position:relative;display:flex;flex-direction:column;align-items:center;justify-content:center;text-align:center;color:#fff}
.hero-photo{position:absolute;inset:0;background:radial-gradient(ellipse at center,#4a4c4d 0%,#222324 60%,#111 100%)}
.hero h1{position:relative;font-size:58px;font-weight:500;line-height:1.15;letter-spacing:1px}
.hero .btn{position:relative;margin-top:26px}

/* about */
.about{height:300px;background:var(--mist);display:flex;flex-direction:column;align-items:center;justify-content:center;text-align:center;padding:0 280px}
.about .eyebrow{color:var(--ink);font-size:11px}
.about .brand{margin:8px 0 14px;font-size:40px}
.about p{font-size:13px;line-height:1.7;color:#333}
.about .btn{margin-top:18px}

/* services */
.services{height:480px;position:relative;display:flex;flex-direction:column;align-items:center;padding-top:46px}
.road-photo{position:absolute;left:0;right:0;bottom:0;height:240px;background:linear-gradient(180deg,#ffffff 0%,#c9cfd2 55%,#8d9498 100%)}
.services h2{font-size:40px;font-weight:700;margin:4px 0 30px}
.cards{position:relative;display:flex;gap:30px}
.card{width:270px;background:#fff;box-shadow:0 6px 20px rgba(0,0,0,.12);padding:26px 24px;display:flex;gap:16px}
.card .icon{flex:none;width:56px;height:56px;border-radius:50%;background:var(--ink);display:flex;align-items:center;justify-content:center}
.card h3{font-size:16px;font-weight:500;line-height:1.3;margin-bottom:8px}
.card p{font-size:12px;line-height:1.6;color:var(--muted)}
.call{position:relative;margin-top:40px;text-align:center}
.call p{font:500 20px "Oswald",sans-serif}
.call .phone{display:flex;align-items:center;gap:8px;justify-content:center;font:700 30px "Oswald",sans-serif;color:var(--green)}

/* products */
.products{height:330px;display:flex;position:relative;overflow:hidden;background:var(--green)}
.product{flex:1;display:flex;flex-direction:column;align-items:center;justify-content:center;color:#fff;text-align:center;padding:0 60px}
.product h3{font-size:30px;font-weight:500}
.product p{font-size:12px;line-height:1.6;margin-top:8px;max-width:260px}
.product-fuel{background:linear-gradient(160deg,#27a84c,#137a33)}
.product-wire{background:linear-gradient(160deg,#2e3133,#151617);clip-path:polygon(18% 0,100% 0,82% 100%,0 100%);margin:0 -70px;z-index:1}
.product-more{background:linear-gradient(160deg,#22a046,#0f6e2d)}

/* testimonials */
.testimonials{height:380px;display:flex;flex-direction:column;align-items:center;justify-content:center;text-align:center;padding:0 300px}
.testimonials h2{font-size:36px;font-weight:700;margin:4px 0 18px}
.testimonials blockquote{font-size:14px;line-height:1.75;color:#444;font-style:italic}
.avatars{display:flex;gap:14px;align-items:center;margin-top:22px}
.avatar{width:44px;height:44px;border-radius:50%;background:linear-gradient(135deg,#b8c0c4,#8c959a)}
.avatar.active{width:58px;height:58px;border:3px solid var(--green)}
.reviewer{margin-top:12px;font:600 12px "Open Sans",sans-serif;text-transform:uppercase}
.reviewer span{display:block;color:var(--muted);font-weight:400;text-transform:none}

/* counter */
.counter{height:330px;background:var(--green);position:relative;overflow:hidden;padding:70px 0 0 120px;color:#fff}
.track-art{position:absolute;right:-40px;top:-20px;width:620px;height:380px;background:linear-gradient(120deg,rgba(255,255,255,.05),rgba(255,255,255,.55));transform:skewX(-18deg)}
.counter h2{position:relative;font-size:26px;font-weight:500}
.counter .total{position:relative;font:700 104px "Oswald",sans-serif;color:var(--char);letter-spacing:3px;line-height:1.1}
.counter .btn{position:relative;background:var(--ink);margin-top:12px}

/* footer */
.site-footer{height:444px;background:var(--grey);padding:60px 120px 0;display:flex;flex-direction:column}
.footer-grid{display:flex;gap:80px}
.footer-brand{width:280px}
.footer-brand p{font-size:12px;line-height:1.7;color:var(--muted);margin-top:14px}
.footer-col h3,.footer-form h3{font-size:16px;font-weight:500;margin-bottom:16px}
.footer-col li{list-style:none;display:flex;align-items:center;gap:10px;font-size:13px;margin-bottom:12px}
.footer-col .social{margin-top:6px}
.footer-form{flex:1}
.fields{display:grid;grid-template-columns:1fr 1fr;gap:10px}
.field{background:#fff;border:1px solid #d6dadc;height:36px;font-size:12px;color:#888;padding:9px 12px}
.field.wide{grid-column:1/3;height:80px}
.footer-form .btn{margin-top:12px}
.copyright{margin-top:auto;border-top:1px solid #d6dadc;padding:20px 0;font-size:12px;color:var(--muted)}
</style>
</head>
<body>
<div class="page">

<header class="site-header">
  <div class="brand"><span class="dot"></span>GraniteLoop</div>
  <nav class="nav"><span>Home</span><span>About Us</span><span>Services</span><span>Contact Us</span></nav>
  <div class="header-contact">
    <div><strong>(555) 014-2786</strong>info@graniteloop.example</div>
    <div class="social"><span></span><span></span><span></span></div>
  </div>
</header>

<section class="hero">
  <div class="hero-photo" role="img" aria-label="Large pile of used waste tires"></div>
  <h1>Powering Innovation,<br>One Tire at a Time</h1>
  <span class="btn">Learn More</span>
</section>

<section class="about">
  <span class="eyebrow">Welcome to</span>
  <div class="brand"><span class="dot"></span>GraniteLoop</div>
  <p>GraniteLoop is a waste tire recycling company focused on sustainable, cost effective service. We collect, shred and process used tires into useful materials, helping businesses keep tires out of landfills while saving time and money.</p>
  <span class="btn">Learn More</span>
</section>

<section class="services">
  <div class="road-photo" role="img" aria-label="Open highway road stretching into the distance"></div>
  <span class="eyebrow" style="position:relative">Our Services</span>
  <h2 style="position:relative">What We Do</h2>
  <div class="cards">
    <div class="card">
      <div class="icon"><svg width="30" height="30" viewBox="0 0 30 30" fill="none" stroke="#fff" stroke-width="3"><circle cx="15" cy="15" r="12"/><circle cx="15" cy="15" r="5"/></svg></div>
      <div><h3>Waste Tire Management</h3><p>Safe, compliant handling of used tires from pickup to processing.</p></div>
    </div>
    <div class="card">
      <div class="icon"><svg width="32" height="24" viewBox="0 0 32 24" fill="#fff"><rect x="1" y="3" width="18" height="13"/><path d="M20 7h6l5 5v4H20z"/><circle cx="7" cy="19" r="3"/><circle cx="25" cy="19" r="3"/></svg></div>
      <div><h3>Mobile Free Scheduling for Tire Collection</h3><p>Book a pickup in minutes and we arrive on schedule.</p></div>
    </div>
    <div class="card">
      <div class="icon"><svg width="30" height="30" viewBox="0 0 30 30" fill="none" stroke="#fff" stroke-width="3"><path d="M15 4l6 10H9z"/><path d="M5 26h10M15 26h10"/><path d="M4 24l5-8M26 24l-5-8"/></svg></div>
      <div><h3>Mobile Shredding &amp; Special Site Cleanup Services</h3><p>On-site shredding and full cleanup of tire piles anywhere.</p></div>
    </div>
  </div>
  <div class="call">
    <p>Have any Question? Call Us Today!</p>
    <div class="phone"><svg width="24" height="24" viewBox="0 0 24 24" fill="#1c9b43"><path d="M6.6 10.8a15 15 0 006.6 6.6l2.2-2.2a1 1 0 011-.25 11.4 11.4 0 003.6.57 1 1 0 011 1V20a1 1 0 01-1 1A17 17 0 013 4a1 1 0 011-1h3.5a1 1 0 011 1c0 1.25.2 2.45.57 3.57a1 1 0 01-.25 1z"/></svg>(555) 014-2786</div>
  </div>
</section>

<section class="products">
  <div class="product product-fuel" role="img" aria-label="Shredded tire-derived fuel chips"><h3>Tire-Derived Fuel</h3></div>
  <div class="product product-wire" role="img" aria-label="Bundles of recovered tire wire"><h3>Clean Tire Wire</h3><p>Steel wire recovered from shredded tires, cleaned and ready for reuse.</p></div>
  <div class="product product-more" role="img" aria-label="Recycled rubber materials"><h3>Further Materials</h3></div>
</section>

<section class="testimonials">
  <span class="eyebrow">Client Reviews</span>
  <h2>Happy Clients Say</h2>
  <blockquote>“GraniteLoop cleared our yard of old tires fast and on time. Their team was friendly, the pricing was fair, and scheduling pickups is now simple. We recommend them to every shop we know.”</blockquote>
  <div class="avatars">
    <div class="avatar" role="img" aria-label="Client portrait"></div>
    <div class="avatar active" role="img" aria-label="Client portrait"></div>
    <div class="avatar" role="img" aria-label="Client portrait"></div>
  </div>
  <div class="reviewer">Daniel Moreno<span>Shop Owner</span></div>
</section>

<section class="counter">
  <div class="track-art" role="img" aria-label="Tire tread track graphic"></div>
  <h2>Tires Recycled by GraniteLoop</h2>
  <div class="total">6,395,823</div>
  <span class="btn">Learn More</span>
</section>

<footer class="site-footer">
  <div class="footer-grid">
    <div class="footer-brand">
      <div class="brand"><span class="dot"></span>GraniteLoop</div>
      <p>Sustainable tire recycling for businesses across the region.</p>
    </div>
    <div class="footer-col">
      <h3>Contact Us</h3>
      <ul>
        <li><svg width="14" height="14" viewBox="0 0 24 24" fill="#1c9b43"><path d="M6.6 10.8a15 15 0 006.6 6.6l2.2-2.2a1 1 0 011-.25 11.4 11.4 0 003.6.57 1 1 0 011 1V20a1 1 0 01-1 1A17 17 0 013 4a1 1 0 011-1h3.5a1 1 0 011 1c0 1.25.2 2.45.57 3.57a1 1 0 01-.25 1z"/></svg>(555) 014-2786</li>
        <li><svg width="14" height="14" viewBox="0 0 24 24" fill="#1c9b43"><path d="M2 5h20v14H2z"/><path d="M2 5l10 8 10-8" stroke="#fff" stroke-width="2" fill="none"/></svg>info@graniteloop.example</li>
        <li><svg width="14" height="14" viewBox="0 0 24 24" fill="#1c9b43"><path d="M12 2a7 7 0 00-7 7c0 5 7 13 7 13s7-8 7-13a7 7 0 00-7-7zm0 9.5A2.5 2.5 0 1112 6.5a2.5 2.5 0 010 5z"/></svg>4820 Quarry Road, Suite 12, Denver, CO 80216</li>
      </ul>
      <div class="social"><span></span><span></span><span></span></div>
    </div>
    <div class="footer-form">
      <h3>Drop Us Message</h3>
      <div class="fields">
        <div class="field">Name</div>
        <div class="field">Phone</div>
        <div class="field" style="grid-column:1/3">Email</div>
        <div class="field wide">Message</div>
      </div>
      <span class="btn">Send</span>
    </div>
  </div>
  <div class="copyright">© 2024 GraniteLoop. All Rights Reserved.</div>
</footer>

</div>
</body>
</html>
```